Road Construction Company needs business cards

We would like a new business card designed for our business.

We're a road construction company based in Qld, Australia.

Can the business card please have the following information on it.

Name: Brent Halloway
Position: General Manager
Phone: 0491 257 314
Email: Brent.halloway@drovik.com.au
Address: 87 Margrove Ave, Tindale, QLD, 4016
Website: www.drovik.com.au

Visually we'd like the card to be professional and simple.

Attached is our logo.

Our website is www.drovik.com.au

Target Market(s)

Men aged 25-60

Contact Information for Business Card

As listed in project description

Font styles to use
Serif

Requirements
Must have
• Large logo on back of card

```html
<!DOCTYPE html>
<html lang="en">
<head>
<meta charset="utf-8">
<title>Drovik Road Construction – Business Card</title>
<link rel="stylesheet" href="https://fonts.googleapis.com/css2?family=Open+Sans:wght@400;700;800&display=swap">
<style>
  :root {
    --stage: #222222;
    --brand-blue: #1257a6;
    --sky-blue: #45a9dc;
    --edge-blue: #4fb0e6;
    --paper: #ffffff;
    --ink: #0c0f14;
  }
  * { box-sizing: border-box; margin: 0; padding: 0; }
  html, body { width: 1200px; height: 780px; overflow: hidden; }
  body {
    background: var(--stage);
    font-family: "Open Sans", Arial, sans-serif;
    position: relative;
  }
  .card {
    position: absolute;
    width: 520px;
    height: 316px;
    border-radius: 20px;
    overflow: hidden;
    box-shadow: 0 0 0 2px var(--edge-blue), 0 18px 30px rgba(0,0,0,.55);
  }
  .card--back {
    left: 60px; top: 110px;
    background: var(--brand-blue);
    display: flex; align-items: center; justify-content: center;
  }
  .card--front {
    left: 620px; top: 354px;
    background: var(--paper);
  }
  .wordmark {
    font-weight: 800;
    text-transform: uppercase;
    text-align: center;
    line-height: 1;
  }
  .wordmark__name { display: block; font-size: 68px; letter-spacing: 2px; }
  .wordmark__line { display: block; font-size: 15px; letter-spacing: 10px; margin-top: 8px; }
  .card--back .wordmark { color: var(--ink); }
  .card--front .wordmark {
    position: absolute; right: 36px; top: 24px;
    color: var(--brand-blue);
  }
  .card--front .wordmark__name { font-size: 42px; }
  .card--front .wordmark__line { font-size: 10px; letter-spacing: 6.5px; margin-top: 5px; }
  .waves { position: absolute; inset: 0; width: 100%; height: 100%; }
  .contact {
    position: absolute; left: 34px; bottom: 18px;
    color: var(--paper);
  }
  .contact__name { font-size: 20px; font-weight: 700; text-transform: uppercase; letter-spacing: .3px; line-height: 1.1; }
  .contact__role { font-size: 12.5px; line-height: 1.3; margin-top: 1px; }
  .contact__address { font-size: 12px; line-height: 1.3; margin-top: 8px; }
  .contact__list { list-style: none; margin-top: 8px; font-size: 12px; line-height: 1.4; }
  .contact__list li { display: flex; align-items: center; gap: 8px; }
  .contact__icon { width: 11px; height: 11px; flex: none; }
</style>
</head>
<body>

  <section class="card card--back" aria-label="Card back">
    <div class="wordmark">
      <span class="wordmark__name">Drovik</span>
      <span class="wordmark__line">Road Construction</span>
    </div>
  </section>

  <section class="card card--front" aria-label="Card front">
    <svg class="waves" viewBox="0 0 520 316" preserveAspectRatio="none" aria-hidden="true">
      <path fill="var(--brand-blue)" d="M0,122 C120,96 250,112 350,114 C430,116 490,104 520,84 L520,316 L0,316 Z"/>
      <path fill="var(--paper)" d="M0,128 C120,102 250,118 350,120 C430,122 492,108 520,92 L520,316 L0,316 Z"/>
      <path fill="var(--sky-blue)" d="M0,132 C120,108 250,124 350,128 C430,130 492,118 520,104 L520,316 L0,316 Z"/>
      <path fill="var(--paper)" d="M0,146 C120,120 250,134 350,138 C430,140 494,126 520,116 L520,316 L0,316 Z"/>
      <path fill="var(--brand-blue)" d="M0,154 C120,128 250,140 350,144 C430,146 496,132 520,122 L520,316 L0,316 Z"/>
    </svg>

    <div class="wordmark">
      <span class="wordmark__name">Drovik</span>
      <span class="wordmark__line">Road Construction</span>
    </div>

    <div class="contact">
      <p class="contact__name">Brent Halloway</p>
      <p class="contact__role">General Manager</p>
      <p class="contact__address">87 Margrove Ave,<br>Tindale, QLD, 4016</p>
      <ul class="contact__list">
        <li>
          <svg class="contact__icon" viewBox="0 0 24 24" aria-hidden="true"><path fill="#fff" d="M6.6 10.8a15.1 15.1 0 0 0 6.6 6.6l2.2-2.2c.3-.3.7-.4 1-.2 1.1.4 2.3.6 3.6.6.6 0 1 .4 1 1V20c0 .6-.4 1-1 1C10.6 21 3 13.4 3 4c0-.6.4-1 1-1h3.5c.6 0 1 .4 1 1 0 1.3.2 2.5.6 3.6.1.3 0 .7-.2 1z"/></svg>
          0491 257 314
        </li>
        <li>
          <svg class="contact__icon" viewBox="0 0 24 24" aria-hidden="true"><rect x="2" y="5" width="20" height="14" rx="2" fill="#fff"/><path d="M3 6l9 7 9-7" fill="none" stroke="var(--brand-blue)" stroke-width="2"/></svg>
          www.drovik.com.au
        </li>
        <li>
          <svg class="contact__icon" viewBox="0 0 24 24" aria-hidden="true"><circle cx="12" cy="12" r="10" fill="#fff"/><path d="M2 12h20M12 2c3 3 3 17 0 20M12 2c-3 3-3 17 0 20" fill="none" stroke="var(--brand-blue)" stroke-width="1.6"/></svg>
          Brent.halloway@drovik.com.au
        </li>
      </ul>
    </div>
  </section>

</body>
</html>
```